Flyer for Yoga and IronForge.

Just initial idea and open to creativity: I am thinking right half of flyer to be IronForge info and left half to be Yoga info.
Feel free to add text as needed but would like following:
Basic text: LotusKeMo $69/mo unlimited sessions.
LotusKEMO.com
IronForge: $99 intro session. Largest IronForge in Texas.
IronForgeKEMO.com

Located Kessel Midtown Houston (KEMO)
Address: 4180 Marlow Pkwy Houston, tx

Please submit any and all designs. Looking to get some great ideas!

Target Market(s)

Young professionals free spirited and fun atmosphere.

Colors
3176b5
85acd3
32a6d7
32b7a4
f59195
cde9f5
f04a50

Requirements
Must have
• Professional yet fun. Text should include:
LotusKeMo and IronForge KeMo taking each a half of the page seperatly get still be identifiable as one. Want to show there is two options for either yoga or IronForge or do both!
IronForge Intro is $99 adm yoga intro is $69.
Nice to have
• Also visit www.ironforgekemo.com for more ideas and info.

```html
<!DOCTYPE html>
<html lang="en">
<head>
<meta charset="utf-8">
<title>IronForge KeMo &amp; LotusKeMo Flyer</title>
<link rel="stylesheet" href="https://fonts.googleapis.com/css2?family=Oswald:wght@400;500;600;700&display=swap">
<style>
  :root {
    --red: #d22c36;
    --teal: #2fb9c9;
    --rule-grey: #5b5d60;
    --ink: #231f20;
    --muted: #4a4a4d;
    --paper: #ffffff;
    --gym-dark: #3a3633;
    --gym-mid: #7a6a5c;
    --gym-light: #c9b9a6;
    --park-sky: #dce9ee;
    --park-tree: #5f7f4a;
    --park-grass: #79b23d;
  }
  * { margin: 0; padding: 0; box-sizing: border-box; }
  html, body {
    width: 828px;
    height: 1200px;
    overflow: hidden;
    background: var(--paper);
  }
  .flyer {
    position: relative;
    width: 828px;
    height: 1200px;
    background: var(--paper);
    font-family: "Oswald", "Arial Narrow", sans-serif;
    text-transform: uppercase;
  }
  .flyer-shapes {
    position: absolute;
    inset: 0;
  }
  .gym-site,
  .yoga-site {
    position: absolute;
    color: var(--paper);
    font-weight: 600;
    font-size: 29px;
    letter-spacing: 0.2px;
    line-height: 1;
    white-space: nowrap;
  }
  .gym-site { left: 45px; top: 50px; }
  .yoga-site { right: 44px; top: 1054px; }

  .offer {
    position: absolute;
    line-height: 1;
  }
  .offer-name {
    font-weight: 600;
    font-size: 34px;
    color: var(--ink);
    letter-spacing: 0.3px;
  }
  .offer-price {
    font-weight: 700;
    font-size: 92px;
    margin-top: 14px;
    letter-spacing: -1px;
  }
  .offer-price small {
    font-size: 40px;
    font-weight: 600;
    letter-spacing: 0;
  }
  .offer-detail {
    font-weight: 500;
    font-size: 24px;
    color: var(--ink);
    margin-top: 12px;
    letter-spacing: 0.3px;
  }
  .offer-note {
    font-weight: 400;
    font-size: 20px;
    color: var(--muted);
    margin-top: 18px;
    line-height: 1.25;
    letter-spacing: 0.2px;
  }
  .gym-offer {
    left: 45px;
    top: 220px;
    width: 270px;
  }
  .gym-offer .offer-price { color: var(--red); }
  .yoga-offer {
    right: 44px;
    top: 640px;
    width: 270px;
    text-align: right;
  }
  .yoga-offer .offer-price { color: var(--teal); }

  .call-to-action {
    position: absolute;
    left: 0;
    right: 0;
    top: 1124px;
    text-align: center;
    color: var(--ink);
    font-weight: 600;
    font-size: 23px;
    letter-spacing: 0.3px;
    line-height: 1;
  }
  .address-bar {
    position: absolute;
    left: 6px;
    right: 9px;
    top: 1165px;
    height: 31px;
    background: var(--red);
    color: var(--paper);
    font-weight: 500;
    font-size: 15px;
    line-height: 31px;
    text-align: center;
    letter-spacing: 0.2px;
  }
</style>
</head>
<body>
<main class="flyer">
  <svg class="flyer-shapes" width="828" height="1200" viewBox="0 0 828 1200">
    <defs>
      <linearGradient id="gym-tones" x1="0" y1="0" x2="1" y2="1">
        <stop offset="0" stop-color="#c9b9a6"/>
        <stop offset="0.45" stop-color="#7a6a5c"/>
        <stop offset="1" stop-color="#3a3633"/>
      </linearGradient>
      <linearGradient id="park-tones" x1="0" y1="0" x2="0" y2="1">
        <stop offset="0" stop-color="#dce9ee"/>
        <stop offset="0.3" stop-color="#5f7f4a"/>
        <stop offset="0.55" stop-color="#79b23d"/>
        <stop offset="1" stop-color="#79b23d"/>
      </linearGradient>
    </defs>

    <rect class="page-frame" x="0.5" y="0.5" width="827" height="1199" fill="none" stroke="#d6d6d6"/>

    <polygon class="gym-banner" points="18,18 638,18 18,163" fill="#d22c36"/>

    <polygon class="gym-photo" role="img"
      aria-label="Photo: members holding plank position on kettlebells in a training gym"
      points="334,15 813,15 813,457 334,556" fill="url(#gym-tones)"/>

    <line class="divider-rule" x1="18" y1="638" x2="813" y2="457"
      stroke="#5b5d60" stroke-width="7"/>

    <polygon class="yoga-photo" role="img"
      aria-label="Photo: outdoor yoga class holding a balancing pose on mats in a park"
      points="18,646 497,537 497,1113 18,1113" fill="url(#park-tones)"/>

    <polygon class="yoga-banner" points="813,968 813,1113 319,1113" fill="#2fb9c9"/>
  </svg>

  <div class="gym-site">IronForgeKEMO.com</div>

  <section class="offer gym-offer">
    <h2 class="offer-name">IronForge KeMo</h2>
    <p class="offer-price">$99</p>
    <p class="offer-detail">Intro Session</p>
    <p class="offer-note">Largest IronForge in Texas</p>
  </section>

  <section class="offer yoga-offer">
    <h2 class="offer-name">LotusKeMo</h2>
    <p class="offer-price">$69<small>/mo</small></p>
    <p class="offer-detail">Unlimited Sessions</p>
    <p class="offer-note">Do yoga, IronForge<br>or do both!</p>
  </section>

  <div class="yoga-site">LotusKEMO.com</div>

  <p class="call-to-action">Visit us today for more information and follow us on Pagebook!</p>

  <div class="address-bar">Located Kessel Midtown Houston (KEMO) Address: 4180 Marlow Pkwy Houston, TX</div>
</main>
</body>
</html>
```